Pagecraft Design for Fruit & Veggie Swap Site

I need a pagecraft design for the HOME PAGE of a company located in Kona, Hawaii called Leafway Exchange Hawaii. Leafway Exchange Hawaii (LEH) is a site intended to support the local food movement by connecting neighbors in order for them to swap/trade produce from their farm or garden. The purpose of this site is to support sustainable agriculture in Hawaii and encourage community interaction.

The model of the site is similar to:
http://www.harvtrade.me/ (I really like the simple design of this site)
http://www.plotbarter.co.uk/ (I don't like the design of this site, just the functionality. The design is too busy and unbalanced.)
Unlike the two sites listed above, however, LEH is only targeted at people living on the Big Island of Hawaii.

The site is simply intended to be a platform to connect people, then they are free to swap or barter off site, similar to the way postboardly connects people. Users can create "posts" for crops that they have available for swap, which are searchable based on name and location.

I have created a very basic, no-css, dev version of the site to work on the back end, which is located here: http://leafwayexchangehawaii.com/test
Feel free to register and create a test post to get a feel for how it works.

The images I have uploaded are just for ideas and do not have to be in the design.

Target Market(s)

The targeted audience is gardeners and farmers on the Big Island of Hawaii. These people are quite varied in age and technical ability.

Industry/Entity Type

Agriculture

Requirements
Must have
• On the homepage, I would like to have a list of the most recent "posts", displayed as the post title, with the most recent post at the top of the list. In the test site, this is located in the right column, but it doesn't have to be in that location in the final design.

I would also like the option to "Add new listing" to be displayed creatively on the home page. This can be in the form of a graphic that links to a form on another page.

I would also like to have a search box on the homepage. Users can search by crop name and/or location.

The main focal point of the home page will be a Mapsly map application of the Big Island. I am in the process of developing this. You can see the map on the test site, please keep in mind that this map may change slightly in future revisions. Feel free to change the size and styling of the map to fit your design.

I would like the homepage to have a simple and clean layout, making it clear to users how the site works.
For the graphics, I would like to incorporate the "crop circles" idea (yes, like the alien crop circles in fields) with fruits and veggies (including tropical fruit found in Hawaii like banana, coconut, lychee, taro, oranges, as well as traditional vegetables like carrots, lettuce, etc.), and also potentially with the idea of sharing and circulating produce with neighbors.
Please note that those specific fruits and veggies don't need to be used, or that many of them, I was just giving them as examples.

I would also like to have a place on the homepage where users can login/sign up. This can be a login form with a sign up link, or a login link and a sign up link.

I would like the entire design to fit on a page without having to scroll.

Once the site has a substantial user base, I plan to incorporate advertising. Please create a design that will be easy to integrate ads into in the future, most likely in the side bar or footer. I do not want the original design to have ad space, just the ability to add it easily in the future and having it look good with the current design.

```html
<!DOCTYPE html>
<html lang="en">
<head>
<meta charset="utf-8">
<title>Leafway Exchange Hawaii – Home</title>
<link rel="stylesheet" href="https://fonts.googleapis.com/css2?family=Cedarville+Cursive&family=Chewy&family=Fontdiner+Swanky&display=swap">
<style>
  :root {
    --meadow-light: #f1f0e4;
    --meadow-mid: #d6e6cf;
    --meadow-deep: #a9c9a0;
    --meadow-dry: #c9b38f;
    --paper: #cc915c;
    --paper-light: #d49d68;
    --paper-edge: #b97c48;
    --ink-brown: #5a3114;
    --logo-brown: #6e3f1e;
    --grass-dark: #1f2f1a;
    --grass-mid: #3d5330;
    --grass-light: #5b7044;
    --cucumber: #6cae3e;
    --cucumber-dark: #3c7023;
    --white: #ffffff;
    --map-sea: #a9c3e2;
    --map-sea-light: #c3d5ea;
    --map-frame: #7d5430;
  }
  * { box-sizing: border-box; margin: 0; padding: 0; }
  html, body { width: 1200px; height: 747px; overflow: hidden; }
  body {
    position: relative;
    background:
      radial-gradient(ellipse 60% 55% at 50% 45%, var(--meadow-light) 0%, transparent 70%),
      linear-gradient(to right, var(--meadow-deep), var(--meadow-mid) 18%, var(--meadow-mid) 82%, var(--meadow-deep));
    font-family: "Cedarville Cursive", cursive;
    color: var(--ink-brown);
  }
  .meadow-edge {
    position: absolute; inset: 0;
    background:
      linear-gradient(to bottom, rgba(150,140,100,.45), transparent 10%),
      linear-gradient(to top, rgba(150,130,95,.55), transparent 14%);
  }
  .brand {
    position: absolute; left: 0; width: 1200px; top: 48px;
    text-align: center; font-size: 46px; color: var(--logo-brown);
  }
  .paper-panel {
    position: absolute; left: 189px; top: 146px; width: 866px; height: 610px;
    background:
      radial-gradient(ellipse at 40% 40%, var(--paper-light), transparent 70%),
      var(--paper);
    border-radius: 16px 12px 0 0;
    box-shadow: 0 0 8px rgba(120,80,40,.45);
  }
  .panel-grass {
    position: absolute; left: 189px; top: 650px; width: 866px; height: 97px;
    background: linear-gradient(to bottom, transparent, rgba(170,160,120,.55) 60%, rgba(150,140,105,.8));
  }
  .produce-art {
    position: absolute; left: 126px; top: 112px; width: 166px; height: 124px;
    border-radius: 48% 52% 45% 55%;
    background: radial-gradient(ellipse at 50% 45%, #e8c850 0%, #8fb24a 55%, rgba(143,178,74,0) 75%);
  }
  .main-nav a, .login-link {
    position: absolute; top: 172px; font-size: 21px; color: var(--ink-brown); text-decoration: none;
  }
  .login-link { top: 150px; left: 971px; }
  .section-title {
    position: absolute; font-family: "Fontdiner Swanky", "Chewy", cursive; font-weight: 400;
    font-size: 22px; color: var(--white);
    text-shadow: 0 0 5px rgba(255,255,255,.7);
  }
  .grass-field {
    position: absolute;
    background: radial-gradient(ellipse at 50% 40%, var(--grass-light), var(--grass-mid) 45%, var(--grass-dark));
    border-radius: 38% 42% 36% 40% / 50%;
    color: var(--white); font-size: 17px; padding: 11px 18px;
  }
  .cucumber-button {
    position: absolute; background: radial-gradient(ellipse at 60% 35%, #9fd46a, var(--cucumber) 40%, var(--cucumber-dark));
    border-radius: 50%; color: var(--white); font-size: 17px;
    display: flex; align-items: center; justify-content: center;
  }
  .add-post {
    position: absolute; left: 229px; top: 460px; font-size: 22px; color: var(--ink-brown);
    display: flex; align-items: center; gap: 8px;
  }
  .map-frame {
    position: absolute; left: 483px; top: 336px; width: 303px; height: 254px;
    border: 5px solid var(--map-frame);
    background: linear-gradient(160deg, var(--map-sea-light), var(--map-sea));
  }
  .map-credit {
    position: absolute; right: 3px; bottom: 2px; font-family: Arial, sans-serif;
    font-size: 7px; color: #333;
  }
  .recent-posts {
    position: absolute; left: 845px; top: 266px; width: 202px; height: 356px;
    background: radial-gradient(ellipse at 50% 40%, var(--grass-light), var(--grass-mid) 45%, var(--grass-dark));
    border-radius: 16px 20px 14px 18px; padding: 14px 20px;
    list-style: none; text-align: center;
    font-family: Arial, Helvetica, sans-serif; font-size: 12.6px; line-height: 14.8px; color: var(--white);
  }
  .copyright { position: absolute; left: 288px; top: 661px; font-size: 12px; }
  .social-links { position: absolute; left: 948px; top: 663px; display: flex; gap: 6px; }
  .social-links span { width: 17px; height: 17px; background: var(--ink-brown); border-radius: 2px; }
</style>
</head>
<body>
  <div class="meadow-edge" role="img" aria-label="Grass border framing the page"></div>
  <div class="brand">Leafway Exchange</div>

  <div class="paper-panel"></div>
  <div class="panel-grass" role="img" aria-label="Grass growing along the bottom of the panel"></div>
  <div class="produce-art" role="img" aria-label="Illustration of cucumber, onion and tomato"></div>

  <nav class="main-nav">
    <a href="#" style="left:407px">Home</a>
    <a href="#" style="left:502px">About Us</a>
    <a href="#" style="left:660px">Blog</a>
    <a href="#" style="left:755px">Contact Us</a>
  </nav>
  <a class="login-link" href="#">Login</a>

  <h2 class="section-title" style="left:228px;top:242px">Sign Up</h2>
  <div class="grass-field" style="left:220px;top:292px;width:193px;height:42px">Name</div>
  <div class="grass-field" style="left:220px;top:337px;width:193px;height:42px">Email</div>
  <div class="cucumber-button" style="left:342px;top:390px;width:71px;height:34px">Go</div>

  <div class="add-post">
    <svg width="22" height="22" viewBox="0 0 22 22" aria-hidden="true">
      <path d="M11 2v18M2 11h18" stroke="#5a3114" stroke-width="4" stroke-linecap="round"/>
    </svg>
    Add New Post
  </div>

  <h2 class="section-title" style="left:477px;top:237px">Search</h2>
  <div class="grass-field" style="left:481px;top:270px;width:191px;height:46px">Search for</div>
  <div class="cucumber-button" style="left:707px;top:281px;width:70px;height:34px">Search</div>

  <div class="map-frame" role="img" aria-label="Map of the Big Island of Hawaii with produce post pins">
    <span class="map-credit">Map data ©2013 Mapsly · Terms of Use</span>
  </div>

  <h2 class="section-title" style="left:850px;top:230px">Recent Posts</h2>
  <ul class="recent-posts">
    <li>Lemons (Pahala)</li>
    <li>Oranges (Kohala)</li>
    <li>Coconuts (hilo)</li>
    <li>Lettuce (Holualoa)</li>
    <li>Testuser trying to add photo (Hawi)</li>
    <li>New post from testuser with map and photo (honokaa)</li>
    <li>New post from testuser (honokaa)</li>
    <li>Papaya seedlings (captain cook)</li>
    <li>2 Dozen Organic Eggs (Kealakekua)</li>
    <li>Coffee cherries (kapoho)</li>
    <li>Bamboo plants (Captain Cook)</li>
    <li>Kona limes (pahoa)</li>
    <li>Mango (pahoa)</li>
    <li>Taro root (pahoa)</li>
    <li>Pineapple (Naalehu)</li>
  </ul>

  <div class="copyright">Copyright 2013</div>
  <div class="social-links" aria-label="Social links">
    <span></span><span></span><span></span><span></span>
  </div>
</body>
</html>
```